Visitenkarte erstellen für Reiki Praxis

Visitenkarten für Reiki Praxis Doppelseitig

business cards reiki practice double-sided

The background can also be a different color

```html
<!DOCTYPE html>
<html lang="en">
<head>
<meta charset="UTF-8">
<title>Lumen Balance – Business Cards</title>
<link href="https://fonts.googleapis.com/css2?family=Poppins:wght@400;500;600&display=swap" rel="stylesheet">
<style>
  :root {
    --stage: #1c1c1c;
    --stage-edge: #0e0e0e;
    --card: #0b0b0b;
    --card-edge: #2a2a2a;
    --ink: #f5f5f5;
    --gold: #e2a52a;
    --divider: #3a3a3a;
  }
  * { margin: 0; padding: 0; box-sizing: border-box; }
  html, body {
    width: 1200px;
    height: 900px;
    overflow: hidden;
  }
  body {
    background: radial-gradient(ellipse at 50% 40%, var(--stage) 0%, var(--stage-edge) 100%);
    font-family: "Poppins", sans-serif;
    display: flex;
    flex-direction: column;
    align-items: center;
    justify-content: center;
    gap: 40px;
  }
  .card {
    width: 700px;
    height: 400px;
    background: var(--card);
    border: 1px solid var(--card-edge);
    box-shadow: 0 18px 40px rgba(0,0,0,0.6);
    position: relative;
    color: var(--ink);
  }

  /* Brand lockup */
  .brand {
    display: flex;
    flex-direction: column;
    align-items: center;
    gap: 16px;
  }
  .brand-dot {
    width: 44px;
    height: 44px;
    border-radius: 50%;
    border: 2px solid var(--ink);
  }
  .brand-name {
    font-weight: 500;
    color: var(--ink);
    letter-spacing: 0.04em;
    text-transform: uppercase;
    white-space: nowrap;
  }

  /* Contact side */
  .card-contact {
    display: flex;
  }
  .contact-brand {
    width: 46%;
    display: flex;
    align-items: center;
    justify-content: center;
  }
  .contact-brand .brand-name { font-size: 26px; }
  .contact-divider {
    width: 1px;
    margin: 60px 0;
    background: var(--divider);
  }
  .contact-details {
    flex: 1;
    padding: 0 40px;
    display: flex;
    flex-direction: column;
    justify-content: center;
  }
  .person-name {
    color: var(--gold);
    font-weight: 600;
    font-size: 22px;
    letter-spacing: 0.02em;
    text-transform: uppercase;
    line-height: 1.1;
  }
  .person-role {
    font-size: 17px;
    margin-bottom: 22px;
  }
  .contact-list {
    list-style: none;
    font-size: 16px;
    line-height: 1.55;
  }
  .contact-list li {
    display: flex;
    align-items: center;
    gap: 10px;
  }
  .contact-list svg {
    width: 16px;
    height: 16px;
    flex: none;
    fill: var(--gold);
  }
  .address {
    margin-top: 20px;
    font-size: 16px;
    line-height: 1.45;
    font-style: normal;
  }

  /* Logo side */
  .card-logo {
    display: flex;
    align-items: center;
    justify-content: center;
  }
  .card-logo .brand-name { font-size: 40px; }
</style>
</head>
<body>

  <section class="card card-contact">
    <div class="contact-brand">
      <div class="brand">
        <span class="brand-dot"></span>
        <span class="brand-name">Lumen Balance</span>
      </div>
    </div>
    <div class="contact-divider"></div>
    <div class="contact-details">
      <h2 class="person-name">Daniel Hart</h2>
      <p class="person-role">Managing Director</p>
      <ul class="contact-list">
        <li>
          <svg viewBox="0 0 24 24" aria-hidden="true"><path d="M6.6 10.8a15.1 15.1 0 0 0 6.6 6.6l2.2-2.2a1 1 0 0 1 1-.25 11.4 11.4 0 0 0 3.6.57 1 1 0 0 1 1 1V20a1 1 0 0 1-1 1A17 17 0 0 1 3 4a1 1 0 0 1 1-1h3.5a1 1 0 0 1 1 1c0 1.25.2 2.45.57 3.57a1 1 0 0 1-.25 1z"/></svg>
          030-555 018 274
        </li>
        <li>
          <svg viewBox="0 0 24 24" aria-hidden="true"><path d="M2 5h20v14H2z M2 5l10 8 10-8" fill="none" stroke="#e2a52a" stroke-width="2"/><path d="M2 5h20l-10 8z"/></svg>
          hello@lumenbalance.de
        </li>
        <li>
          <svg viewBox="0 0 24 24" aria-hidden="true"><circle cx="12" cy="12" r="9.5" fill="none" stroke="#e2a52a" stroke-width="2"/><path d="M2.5 12h19M12 2.5c3 3 3 16 0 19M12 2.5c-3 3-3 16 0 19" fill="none" stroke="#e2a52a" stroke-width="1.6"/></svg>
          www.lumenbalance.de
        </li>
      </ul>
      <address class="address">
        17, Lindenweg Studio 2<br>
        10115,Germany
      </address>
    </div>
  </section>

  <section class="card card-logo">
    <div class="brand">
      <span class="brand-dot"></span>
      <span class="brand-name">Lumen Balance</span>
    </div>
  </section>

</body>
</html>
```